Need DL Flyer for Real Estate Drops

We need a real estate flyer ,double sided. With content on 1 side like: Want to know what's your house is worth " contact us today and on other side agent details. We are looking for an ongoing partnership with designer so this assignment will be ongoing

```html
<!DOCTYPE html>
<html lang="en">
<head>
<meta charset="utf-8">
<title>Corvale Real Estate – DL Flyer</title>
<link href="https://fonts.googleapis.com/css2?family=Oswald:wght@300;400;600;700&family=Saira+Condensed:wght@400;500;600;700&display=swap" rel="stylesheet">
<style>
  :root{
    --stage:#585858;
    --navy:#141c3a;
    --navy-deep:#0f1530;
    --red:#c8202c;
    --red-dark:#8e1a24;
    --white:#ffffff;
    --grey:#d9d9d9;
  }
  *{margin:0;padding:0;box-sizing:border-box}
  html,body{width:1200px;height:1177px;overflow:hidden;background:var(--stage)}
  .stage{position:relative;width:1200px;height:1177px}
  .flyer{position:absolute;top:106px;width:475px;height:954px;overflow:hidden;background:var(--white);box-shadow:0 4px 14px rgba(0,0,0,.35)}
  .flyer--front{left:95px}
  .flyer--back{left:631px;background:var(--navy)}
  .flyer__bg{position:absolute;inset:0;width:475px;height:954px}
  .abs{position:absolute}

  /* front */
  .hero-photo{position:absolute;left:0;top:50px;width:475px;height:330px;
    background:linear-gradient(180deg,#c9d4de 0%,#e9d3b8 22%,#7f8d57 40%,#b2683a 62%,#8a4a2c 80%,#5c4a3c 100%)}
  .headline-banner{position:absolute;left:17px;top:0;width:443px;height:89px;border-radius:0 0 14px 14px;
    background:linear-gradient(90deg,var(--red-dark),var(--red));display:flex;align-items:center;justify-content:center}
  .headline-banner__text{font-family:"Oswald",sans-serif;font-weight:600;font-size:62px;color:var(--white);letter-spacing:.5px;line-height:1}
  .pitch{position:absolute;left:0;width:475px;text-align:center;color:var(--white);font-family:"Oswald",sans-serif}
  .pitch__lead{top:618px;font-weight:300;font-size:44px;line-height:1}
  .pitch__worth{top:672px;font-weight:700;font-size:68px;line-height:1}
  .pitch__rule{position:absolute;left:118px;top:754px;width:240px;height:2px;background:var(--red)}
  .pitch__cta{top:762px;font-weight:300;font-size:32px;line-height:1}
  .brand{position:absolute;display:flex;align-items:center;gap:12px;font-family:"Saira Condensed",sans-serif;font-weight:600;line-height:1;white-space:nowrap}
  .brand__mark{display:block}
  .brand--front{left:0;width:475px;justify-content:center;top:866px;color:var(--navy);font-size:32px}
  .brand--front .brand__mark{width:34px;height:34px;background:var(--red)}
  .site{position:absolute;left:0;width:475px;text-align:center;font-family:"Saira Condensed",sans-serif;font-weight:700;line-height:1}
  .site--front{top:918px;font-size:24px;color:var(--navy)}

  /* back */
  .house-photo{position:absolute;left:0;top:420px;width:475px;height:460px;
    background:linear-gradient(180deg,rgba(40,50,80,.0) 0%,rgba(70,80,110,.45) 35%,rgba(50,60,90,.35) 70%,rgba(20,28,58,0) 100%)}
  .portrait{position:absolute;left:17px;top:500px;width:182px;height:370px;
    background:linear-gradient(180deg,#9a9a9a 0%,#c9c9c9 30%,#b3b3b3 60%,#8c8c8c 100%)}
  .brand--back{left:0;width:475px;justify-content:center;top:66px;color:var(--white);font-size:46px;gap:16px}
  .brand--back .brand__mark{width:50px;height:50px;background:var(--navy)}
  .agent__name{position:absolute;left:0;top:306px;width:475px;text-align:center;font-family:"Oswald",sans-serif;font-weight:600;font-size:62px;color:var(--white);line-height:1.2}
  .agent__role{position:absolute;left:0;top:392px;width:475px;text-align:center;font-family:"Oswald",sans-serif;font-weight:300;font-size:32px;color:var(--red);line-height:1.2}
  .contact{position:absolute;left:198px;display:flex;align-items:flex-start;gap:8px;color:var(--white);font-family:"Saira Condensed",sans-serif;line-height:1.15}
  .contact__icon{width:16px;height:16px;flex:none;margin-top:4px}
  .contact--phone{top:532px;font-size:26px}
  .contact--mobile{top:566px;font-size:26px}
  .contact--email{top:630px;font-size:19px}
  .contact--email .contact__icon{margin-top:2px}
  .contact--address{top:680px;font-size:20px}
  .social{position:absolute;left:418px;width:40px;height:40px;border-radius:50%}
  .social--one{top:796px;background:#3a5aa8}
  .social--two{top:845px;background:var(--red)}
  .globe{position:absolute;left:227px;top:884px;width:20px;height:20px}
  .site--back{top:912px;font-size:24px;color:var(--white)}
</style>
</head>
<body>
<main class="stage">

  <!-- Front side -->
  <section class="flyer flyer--front">
    <div class="hero-photo" role="img" aria-label="Aerial view of a village with red-roofed houses and autumn trees"></div>
    <svg class="flyer__bg" viewBox="0 0 475 954" aria-hidden="true">
      <path d="M0 370 Q240 300 475 350 L475 870 Q230 790 0 880 Z" fill="var(--navy)"/>
      <path d="M0 555 Q250 650 475 470 L475 495 Q250 690 0 585 Z" fill="var(--red)"/>
      <path d="M0 868 Q200 770 475 835 L475 954 L0 954 Z" fill="var(--white)"/>
      <path d="M0 848 Q210 740 475 818 L475 836 Q210 770 0 885 Z" fill="var(--red)"/>
    </svg>
    <svg class="flyer__bg" viewBox="0 0 475 954">
      <defs>
        <linearGradient id="photoHouse" x1="0" y1="0" x2="0" y2="1">
          <stop offset="0" stop-color="#7b8fb8"/><stop offset=".55" stop-color="#3e4a6c"/><stop offset="1" stop-color="#6c6a6a"/>
        </linearGradient>
        <linearGradient id="photoLawn" x1="0" y1="0" x2="0" y2="1">
          <stop offset="0" stop-color="#c7d5e2"/><stop offset=".5" stop-color="#9a7d64"/><stop offset="1" stop-color="#4f9a3a"/>
        </linearGradient>
        <linearGradient id="photoInterior" x1="0" y1="0" x2="0" y2="1">
          <stop offset="0" stop-color="#f1efea"/><stop offset=".6" stop-color="#ddd5c8"/><stop offset="1" stop-color="#b9a58c"/>
        </linearGradient>
      </defs>
      <g role="img" aria-label="Photo of a two-storey house at dusk">
        <circle cx="112" cy="413" r="90" fill="var(--red)"/>
        <circle cx="112" cy="413" r="84" fill="var(--white)"/>
        <circle cx="112" cy="413" r="78" fill="url(#photoHouse)"/>
      </g>
      <g role="img" aria-label="Photo of an interior living room">
        <circle cx="371" cy="413" r="90" fill="var(--red)"/>
        <circle cx="371" cy="413" r="84" fill="var(--white)"/>
        <circle cx="371" cy="413" r="78" fill="url(#photoInterior)"/>
      </g>
      <g role="img" aria-label="Photo of a house with a green lawn">
        <circle cx="229" cy="486" r="88" fill="var(--navy-deep)"/>
        <circle cx="229" cy="486" r="82" fill="var(--white)"/>
        <circle cx="229" cy="486" r="76" fill="url(#photoLawn)"/>
      </g>
    </svg>

    <div class="headline-banner"><span class="headline-banner__text">WANT TO KNOW</span></div>

    <p class="pitch pitch__lead">What’s Your Property</p>
    <p class="pitch pitch__worth">WORTH?</p>
    <span class="pitch__rule"></span>
    <p class="pitch pitch__cta">Contact Us Today!</p>

    <div class="brand brand--front"><span class="brand__mark"></span><span>Corvale Real Estate</span></div>
    <p class="site site--front">www.corvalerealestate.com.au</p>
  </section>

  <!-- Back side -->
  <section class="flyer flyer--back">
    <div class="house-photo" role="img" aria-label="Faint photo of a modern house behind the agent"></div>
    <svg class="flyer__bg" viewBox="0 0 475 954" aria-hidden="true">
      <path d="M0 0 H475 V362 Q320 262 0 330 Z" fill="var(--red)"/>
      <path d="M50 298 Q270 250 475 338 L475 360 Q280 278 50 298 Z" fill="var(--white)"/>
    </svg>
    <div class="portrait" role="img" aria-label="Black and white portrait of the agent in a suit"></div>
    <svg class="flyer__bg" viewBox="0 0 475 954" aria-hidden="true">
      <path d="M0 880 Q210 810 475 852 L475 954 L0 954 Z" fill="var(--white)"/>
      <path d="M0 912 Q230 842 475 880 L475 954 L0 954 Z" fill="var(--red)"/>
    </svg>

    <div class="brand brand--back"><span class="brand__mark"></span><span>Corvale Real Estate</span></div>

    <h1 class="agent__name">Arjun Kalra</h1>
    <p class="agent__role">Managing Director/LEA</p>

    <p class="contact contact--phone">
      <svg class="contact__icon" viewBox="0 0 16 16" aria-hidden="true"><path d="M3.5 1.5l2.6 2.4-1.4 2.2c.9 2 2.6 3.8 4.7 4.7l2.2-1.4 2.4 2.6-1.8 2C6.6 13.6 2.4 9.4 1.5 3.3z" fill="var(--red)"/></svg>
      <span>03 9120 4477</span>
    </p>
    <p class="contact contact--mobile">
      <svg class="contact__icon" viewBox="0 0 16 16" aria-hidden="true"><rect x="4" y="1" width="8" height="14" rx="1.5" fill="none" stroke="var(--red)" stroke-width="1.6"/><circle cx="8" cy="12.4" r=".9" fill="var(--red)"/></svg>
      <span>0400163829</span>
    </p>
    <p class="contact contact--email">
      <svg class="contact__icon" viewBox="0 0 16 16" aria-hidden="true"><rect x="1.5" y="3.5" width="13" height="9" rx="1" fill="none" stroke="var(--red)" stroke-width="1.4"/><path d="M2 4.5l6 4.5 6-4.5" fill="none" stroke="var(--red)" stroke-width="1.4"/></svg>
      <span>arjun@corvalerealestate.com.au</span>
    </p>
    <p class="contact contact--address">
      <svg class="contact__icon" viewBox="0 0 16 16" aria-hidden="true"><path d="M8 1a5 5 0 0 0-5 5c0 3.6 5 9 5 9s5-5.4 5-9a5 5 0 0 0-5-5zm0 7a2 2 0 1 1 0-4 2 2 0 0 1 0 4z" fill="var(--red)"/></svg>
      <span>14/8 Horizon Way<br>Kelvale 3030</span>
    </p>

    <span class="social social--one"></span>
    <span class="social social--two"></span>

    <svg class="globe" viewBox="0 0 20 20" aria-hidden="true"><circle cx="10" cy="10" r="8" fill="none" stroke="var(--navy)" stroke-width="1.6"/><ellipse cx="10" cy="10" rx="3.5" ry="8" fill="none" stroke="var(--navy)" stroke-width="1.4"/><path d="M2 10h16M3.5 6h13M3.5 14h13" stroke="var(--navy)" stroke-width="1.2"/></svg>
    <p class="site site--back">www.corvalerealestate.com.au</p>
  </section>

</main>
</body>
</html>
```